Label design: italian artisan honey (to allow tradition look attractive!)

Founded in 1973, this specialized business in artisan honey, is based in Emilia-Romagna. It accounts for 10 apiary locations, honey is organic, whereas the equipment to rise, and control bees are all hand made.
The symbol, (you will find the logo corvasti.ai) is a hexagonal hunting house built in the 17th century. The structure is protected by fine-arts and retains its stucco works and frescoes depicting mythological scenes. The place is located in the hills, next to a hunting area, and surrounded by our ecological farm.

Please find the foto of the label that has been used for over 30 years and also the Italian Beekeeper association label that is placed on all the vases.

Target Market(s)

Local gastronomic shop owners, where local consumers are both young and mature families, well-read, connaisseurs, curious, with strong social ties also with nature.

Font styles to use
Serif
Sans Serif

Requirements
Must have
• We have a glass jar already with specific dimensions.
The lid finishing is metallic finishing, in copper color.
We need the label to have the by-law necessary information of the product on it:
Honey type, producer name, weight, best by date, origin.
The lid measures 6 cm in diameter, and has a border of about 0.5 cm.
The visible part of the glass jar is 3 cm high.
You can get inspired by the type of package we want to use: (in light wood or carton board as materials as in the 2 examples we attach is actually like a matchbox).
We also attached an illustrator file with the logo shape, colors to be adapted to your design, consider the "grey color" and the "metallic finishing" on the corner, as shown in the file ref_glimboard_3.
Nice to have
• The _pack_1 and _pack_3 files are mood ideas for the box, to provide you inspiration for the label.
The color palette is provided by two files :
ref_glimboard_3 ;
color_palette_corvasti.
The font reference is provided by two files :
Typeface ;
ref_typeface.

```html
<!DOCTYPE html>
<html lang="it">
<head>
<meta charset="utf-8">
<title>Corvasti – Miele Piacentino label</title>
<link rel="stylesheet" href="https://fonts.googleapis.com/css2?family=Josefin+Sans:wght@200;700&display=swap">
<style>
  :root {
    --backdrop: #b97629;
    --navy: #143a4b;
    --gold: #c9935c;
    --gold-light: #e2b57f;
    --band-grey: #cdc5c6;
    --ink-dark: #1d2a2e;
    --flag-green: #3a9a48;
    --flag-white: #f2efe9;
    --flag-red: #d9532c;
  }
  html, body {
    margin: 0;
    padding: 0;
    width: 819px;
    height: 1200px;
    overflow: hidden;
    background: var(--backdrop);
  }
  .label-sheet {
    display: block;
    width: 819px;
    height: 1200px;
  }
  .wordmark {
    font-family: "Josefin Sans", sans-serif;
    font-weight: 200;
    fill: var(--gold);
    letter-spacing: 1px;
  }
  .product-name {
    font-family: "Josefin Sans", sans-serif;
    font-weight: 700;
    fill: var(--gold-light);
  }
  .origin-text {
    font-family: "Josefin Sans", sans-serif;
    font-weight: 700;
    fill: var(--ink-dark);
    letter-spacing: 1px;
  }
  .brand-square {
    fill: none;
    stroke: var(--gold);
    stroke-width: 2;
  }
</style>
</head>
<body>
<svg class="label-sheet" viewBox="0 0 819 1200" xmlns="http://www.w3.org/2000/svg">
  <defs>
    <linearGradient id="flourish-tone" x1="0" x2="1">
      <stop offset="0" stop-color="#c9935c" stop-opacity="0.15"/>
      <stop offset="0.5" stop-color="#c9935c" stop-opacity="0.45"/>
      <stop offset="1" stop-color="#c9935c" stop-opacity="0.15"/>
    </linearGradient>
    <linearGradient id="tricolor" x1="0" x2="1">
      <stop offset="0" stop-color="var(--flag-green)"/>
      <stop offset="0.33" stop-color="var(--flag-green)"/>
      <stop offset="0.45" stop-color="var(--flag-white)"/>
      <stop offset="0.6" stop-color="var(--flag-white)"/>
      <stop offset="0.67" stop-color="var(--flag-red)"/>
      <stop offset="1" stop-color="var(--flag-red)"/>
    </linearGradient>
  </defs>

  <!-- wrap band -->
  <rect class="wrap-band" x="15" y="759" width="789" height="156" fill="var(--band-grey)"
        role="img" aria-label="Fine line floral pattern on pale grey"/>

  <!-- gold flourishes -->
  <rect class="flourish flourish-left" x="276" y="789" width="90" height="42" rx="21" fill="url(#flourish-tone)"
        role="img" aria-label="Gold scroll ornament"/>
  <rect class="flourish flourish-right" x="453" y="789" width="90" height="42" rx="21" fill="url(#flourish-tone)"
        role="img" aria-label="Gold scroll ornament"/>

  <!-- origin ribbon -->
  <g class="origin-ribbon">
    <rect x="349" y="870" width="171" height="24" rx="12" fill="url(#tricolor)" stroke="var(--gold)" stroke-width="2"/>
    <text class="origin-text" x="434.5" y="887" font-size="11" text-anchor="middle">PRODOTTO IN ITALIA</text>
  </g>

  <!-- lid seal with tab -->
  <path class="lid-seal" d="M354 620.6 A171 171 0 1 1 466 620.6 L466 825 L410 849 L354 825 Z"
        fill="var(--navy)" stroke="var(--gold)" stroke-width="3"/>

  <!-- lid disc content -->
  <rect class="brand-square" x="385" y="385" width="50" height="50"/>
  <text class="wordmark" x="410" y="504" font-size="34" text-anchor="middle">CORVASTI</text>
  <text class="product-name" x="410" y="560" font-size="29" text-anchor="middle">MIELE DI</text>
  <text class="product-name" x="410" y="592" font-size="29" text-anchor="middle">ACACIA</text>

  <!-- tab content -->
  <rect class="brand-square" x="397" y="650" width="26" height="26"/>
  <text class="wordmark" x="410" y="703" font-size="15" text-anchor="middle">CORVASTI</text>
  <text class="product-name" x="410" y="790" font-size="15" text-anchor="middle">MIELE</text>
  <text class="product-name" x="410" y="810" font-size="15" text-anchor="middle">PIACENTINO</text>
</svg>
</body>
</html>
```